Small legal and financial translation company needs Squarespace website, brochure and logo

Hello,
We are KLV Services (www.klvservices-example.com), a boutique legal and financial translation company. We offer our services mainly to Spanish customers. Our primary line of business is the translation of financial statements, but we translate a wide variety legal and financial texts.
The project we are offering comprises three parts: a redo of the current website, an informational brochure for potential customer and a logo design. These three parts should provide a consistent image. We would develop content soon.
We are looking for a website that would look like a typical law firm website, nothing too fancy. Right now, it is in English, Spanish and French, although the new site need only be in English and Spanish. There must be good toggling between the English and Spanish versions. There would be no need for tie-ins to social media and it would not contain a blog. Basically, a static site. We aren't interesting in driving traffic to the site or SEO, as we will contact nearly all potential customers beforehand. The website must be built in Squarespace to enable a smooth transition. The content would be similar to the current page, we'll be working on the exact content, but a rough draft is attached.
The brochure will be some three pages and would introduce the company to potential customers, using similar images as the website and the logo to be designed.
The only specifications for the logo is, as the website and brochure, it convey a sense of security and trust.
Feel free to ask with any questions as this is the first time we have used this platform.
Thank you!

I've added a more or less final version for the text in the brochure and updated the brief. Added Wednesday, June 10, 2015

Target Market(s)

Spanish law firms, auditors, accountants, banks, investment firms

Industry/Entity Type

Finance

Logo Text

KLV Services

Number of Pages Required

5+ page

Font styles to use
Serif

Requirements
Must have
• The website must be built in Squarespace and have a good option to toggle between English and Spanish versions.
• Brochure must be in both English and Spanish, I'm attaching a rough draft of the information that it will probably have. This should give an idea about what to include and the spacing. I will update it to include the final information.
Nice to have
• Would be nice to have some quality finance- and legal-related images
Should not have
• Vibrant colours

```html
<!DOCTYPE html>
<html lang="en">
<head>
<meta charset="utf-8">
<title>KLV Services – Brochure Pages 5 and 6</title>
<link rel="stylesheet" href="https://fonts.googleapis.com/css2?family=Cinzel:wght@400&family=Crimson+Text:ital@0;1&family=Open+Sans&family=Arimo&display=swap">
<style>
:root{
  --backdrop:#c8c8c8;
  --paper:#ffffff;
  --maroon:#7a0010;
  --black:#000000;
  --label:#444444;
  --ink:#333333;
  --cell-dark:#d4d5d7;
  --cell-light:#e3e4e6;
  --rule:#c4c4c4;
  --photo-a:#8a6a52;
  --photo-b:#3b2b22;
}
*{margin:0;padding:0;box-sizing:border-box}
html,body{width:1200px;height:1066px;overflow:hidden;background:var(--backdrop)}
.spread{position:relative;width:1200px;height:1066px}
.page-label{position:absolute;top:48px;width:200px;text-align:center;font:28px "Open Sans",sans-serif;color:var(--label)}
.page{position:absolute;top:108px;width:550px;height:850px;background:var(--paper);overflow:hidden}
.page--left{left:54px;box-shadow:-6px 4px 18px rgba(0,0,0,.35)}
.page--right{left:604px;box-shadow:6px 4px 18px rgba(0,0,0,.35)}
.page-title{position:absolute;left:20px;top:34px;font:400 26px "Cinzel",serif;color:var(--maroon);letter-spacing:.5px}
.page--right .page-title{left:28px}

.pricing{position:absolute;left:20px;top:94px;width:508px;border-collapse:collapse;font-family:"Crimson Text",serif;color:var(--ink)}
.pricing th{height:35px;font-size:14px;font-weight:700;color:#222;background:var(--cell-dark)}
.pricing td{height:62.1px;border-top:1px solid rgba(255,255,255,.7)}
.pricing .desc{width:210px;padding-left:19px;font-size:13px;line-height:16px;background:var(--cell-dark)}
.pricing .std{width:155px;text-align:center;font-size:17px;background:var(--cell-light)}
.pricing .adv{text-align:center;font-size:17px;background:var(--cell-dark)}

.footer-band{position:absolute;left:0;bottom:0;width:550px;height:103px}
.footer-url{position:absolute;left:22px;bottom:20px;font:20px "Crimson Text",serif;color:var(--paper)}

.intro{position:absolute;left:32px;top:93px;width:492px;font:13px/18px "Crimson Text",serif;color:var(--ink)}
.testimonial{position:absolute;left:43px;width:475px;height:180px}
.client-photo{position:absolute;left:0;top:0;width:121px;height:121px;border-radius:50%;background:radial-gradient(circle at 50% 40%,var(--photo-a),var(--photo-b))}
.client-name{position:absolute;left:0;top:137px;width:132px;text-align:center;font:15px "Arimo",sans-serif;color:#111}
.quote-mark{position:absolute;font:700 36px/1 Georgia,serif;color:#111}
.quote-mark--open{left:137px;top:-6px}
.quote-mark--close{left:396px;top:122px}
.quote-text{position:absolute;left:163px;top:7px;width:312px;font:italic 13px/18.3px "Crimson Text",serif;color:var(--ink);text-align:justify}
.divider{position:absolute;left:43px;width:472px;height:1px;background:var(--rule)}
</style>
</head>
<body>
<div class="spread">
  <div class="page-label" style="left:237px">Page 5</div>
  <div class="page-label" style="left:783px">Page 6</div>

  <section class="page page--left">
    <h1 class="page-title">Translation Pricing</h1>
    <table class="pricing">
      <thead><tr><th></th><th>Standard</th><th>Advance</th></tr></thead>
      <tbody>
        <tr><td class="desc">Lorem ipsum dolor sit amet,<br>consectetuer adipiscing elit</td><td class="std">$100</td><td class="adv">$200</td></tr>
        <tr><td class="desc">Lorem ipsum dolor sit amet,<br>consectetuer adipiscing elit</td><td class="std">$100</td><td class="adv">$200</td></tr>
        <tr><td class="desc">Lorem ipsum dolor sit amet,<br>consectetuer adipiscing elit</td><td class="std">$100</td><td class="adv">$200</td></tr>
        <tr><td class="desc">Lorem ipsum dolor sit amet,<br>consectetuer adipiscing elit</td><td class="std">$100</td><td class="adv">$200</td></tr>
        <tr><td class="desc">Lorem ipsum dolor sit amet,<br>consectetuer adipiscing elit</td><td class="std">$100</td><td class="adv">$200</td></tr>
        <tr><td class="desc">Lorem ipsum dolor sit amet,<br>consectetuer adipiscing elit</td><td class="std">$100</td><td class="adv">$200</td></tr>
        <tr><td class="desc">Lorem ipsum dolor sit amet,<br>consectetuer adipiscing elit</td><td class="std">$100</td><td class="adv">$200</td></tr>
        <tr><td class="desc">Lorem ipsum dolor sit amet,<br>consectetuer adipiscing elit</td><td class="std">$100</td><td class="adv">$200</td></tr>
        <tr><td class="desc">Lorem ipsum dolor sit amet,<br>consectetuer adipiscing elit</td><td class="std">$100</td><td class="adv">$200</td></tr>
      </tbody>
    </table>
    <svg class="footer-band" viewBox="0 0 550 103" aria-hidden="true">
      <polygon points="0,0 550,100 550,103 0,103" fill="var(--maroon)"/>
      <polygon points="280,50 550,0 550,100" fill="var(--black)"/>
    </svg>
    <div class="footer-url">www.klvservices-example.com</div>
  </section>

  <section class="page page--right">
    <h1 class="page-title">Our Clients</h1>
    <p class="intro">Lorem ipsum dolor sit amet, consectetuer adipiscing elit, sed diam nonummy nibh euismod tincidunt ut laoreet dolore magna aliquam erat volutpat</p>

    <article class="testimonial" style="top:156px">
      <div class="client-photo" role="img" aria-label="Portrait photo of client Daniel Reyes"></div>
      <div class="client-name">Mr. Daniel Reyes</div>
      <span class="quote-mark quote-mark--open">“</span>
      <p class="quote-text">Lorem ipsum dolor sit amet, consectetuer adipiscing elit, sed diam nonummy nibh euismod tincidunt ut laoreet dolore magna aliquam erat volutpat. Ut wisi enim ad minim veniam, quis nostrud exerci tation ullamcorper suscipit lobortis nisl ut aliquip ex ea commodo consequat. Duis autem vel eum iriure dolor in hendrerit in vulputate velit esse molestie consequat, vel illuverofa</p>
      <span class="quote-mark quote-mark--close">”</span>
    </article>
    <div class="divider" style="top:343px"></div>

    <article class="testimonial" style="top:364px">
      <div class="client-photo" role="img" aria-label="Portrait photo of client Daniel Reyes"></div>
      <div class="client-name">Mr. Daniel Reyes</div>
      <span class="quote-mark quote-mark--open">“</span>
      <p class="quote-text">Lorem ipsum dolor sit amet, consectetuer adipiscing elit, sed diam nonummy nibh euismod tincidunt ut laoreet dolore magna aliquam erat volutpat. Ut wisi enim ad minim veniam, quis nostrud exerci tation ullamcorper suscipit lobortis nisl ut aliquip ex ea commodo consequat. Duis autem vel eum iriure dolor in hendrerit in vulputate velit esse molestie consequat, vel illuverofa</p>
      <span class="quote-mark quote-mark--close">”</span>
    </article>
    <div class="divider" style="top:544px"></div>

    <article class="testimonial" style="top:567px">
      <div class="client-photo" role="img" aria-label="Portrait photo of client Daniel Reyes"></div>
      <div class="client-name">Mr. Daniel Reyes</div>
      <span class="quote-mark quote-mark--open">“</span>
      <p class="quote-text">Lorem ipsum dolor sit amet, consectetuer adipiscing elit, sed diam nonummy nibh euismod tincidunt ut laoreet dolore magna aliquam erat volutpat. Ut wisi enim ad minim veniam, quis nostrud exerci tation ullamcorper suscipit lobortis nisl ut aliquip ex ea commodo consequat. Duis autem vel eum iriure dolor in hendrerit in vulputate velit esse molestie consequat, vel illuverofa</p>
      <span class="quote-mark quote-mark--close">”</span>
    </article>

    <svg class="footer-band" viewBox="0 0 550 103" aria-hidden="true">
      <polygon points="0,0 550,100 550,103 0,103" fill="var(--maroon)"/>
      <polygon points="280,50 550,0 550,100" fill="var(--black)"/>
    </svg>
    <div class="footer-url">www.klvservices-example.com</div>
  </section>
</div>
</body>
</html>
```